B2B EDM Banner Design- Specialist Tech Company

We need a new top-of-email banner for our EDM campaigns for Varnel Brix (www.varnelbrix-example.com
). This banner will sit at the top of every email and must immediately signal the brand, look modern and professional, and be visually aligned with the tech/IT audience.
Size of the banner: Around 728x90 - it must fit at the top of an email blast.
Purpose of the Banner
Establish a strong, recognizable brand identity across all Varnel Brix EDMs
visually consistent with existing banners created for other brands (see reference examples provided)
Communicate Varnel Brix’s value proposition at a glance
Brand Name
Varnel Brix
Tagline (must appear in the banner)
“11,322 whitepapers from 726 companies”
Design Requirements
Style & Tone
Modern, clean, and professional
Tech-centric look and feel
High-quality, sleek, and corporate
Eye-catching but not cluttered
Should feel premium and authoritative
Layout & Composition
Full-width banner for email header
Horizontal orientation similar to the Plomtar and Quindle Staff Archive examples
Include space for the brand name/logo prominently on the left or centered
Integrate the tagline in a readable, secondary position
Optional: a subtle background texture or tech-related abstract pattern (circuitry, network nodes, gradient, etc.)
No busy imagery—should feel clean and trustworthy
Color Palette
Use colors consistent with Varnel Brix branding from www.varnelbrix-example.com
Blues, greys, blacks, and tech-style gradients preferred
Should feel consistent with a B2B IT audience
Typography
Clean, sans-serif fonts (professional/tech-aligned)
Brand name should be bold and prominent
Tagline should be smaller, but still readable on desktop and mobile
Imagery (if used)
Abstract tech shapes, network visuals, geometric patterns, or gradient overlays
Avoid photography of people
Keep imagery subtle so text remains legible
Call-to-Action Button (optional)
None required in this banner (unlike the HR examples)
Banner should remain a pure brand header
Deliverables
Final banner in PNG and JPG formats
2–3 design variations (if possible) for A/B testing
Dimensions optimized for EDM: ~600–700px wide (standard email width), proportionate height

```html
<!DOCTYPE html>
<html lang="en">
<head>
<meta charset="utf-8">
<title>Varnel Brix EDM Header Banners</title>
<link rel="stylesheet" href="https://fonts.googleapis.com/css2?family=Montserrat:ital,wght@1,800&family=Open+Sans:wght@300;700&display=swap">
<style>
  :root {
    --page-bg: #ffffff;
    --navy-start: #05408f;
    --navy-mid: #03235c;
    --navy-end: #010a22;
    --grey-start: #c6c6c6;
    --grey-end: #f1f1f1;
    --accent: #1aa3e2;
    --ink-light: #ffffff;
    --ink-dark: #0b3784;
  }
  html, body {
    margin: 0;
    padding: 0;
    width: 1200px;
    height: 1200px;
    overflow: hidden;
    background: var(--page-bg);
  }
  .canvas {
    position: relative;
    width: 1200px;
    height: 1200px;
  }
  .banner {
    position: absolute;
    left: 66px;
    width: 1068px;
    height: 313px;
    overflow: hidden;
    box-shadow: 0 12px 30px rgba(0, 0, 0, 0.18);
  }
  .banner--dark {
    top: 229px;
    background: linear-gradient(90deg, var(--navy-start) 0%, var(--navy-mid) 45%, var(--navy-end) 100%);
  }
  .banner--light {
    top: 657px;
    background: linear-gradient(90deg, var(--grey-start) 0%, #dcdcdc 50%, var(--grey-end) 100%);
  }
  .tech-visual {
    position: absolute;
    left: 480px;
    top: 0;
    width: 588px;
    height: 313px;
  }
  .banner--dark .tech-visual {
    background: radial-gradient(ellipse at 62% 50%, rgba(40, 110, 200, 0.35) 0%, rgba(10, 40, 100, 0.15) 45%, rgba(0, 0, 0, 0) 75%);
  }
  .banner--light .tech-visual {
    background: radial-gradient(ellipse at 62% 50%, rgba(150, 150, 150, 0.30) 0%, rgba(200, 200, 200, 0.12) 45%, rgba(255, 255, 255, 0) 75%);
  }
  .brand-mark {
    position: absolute;
    left: 92px;
    top: 79px;
    width: 76px;
    height: 76px;
    border-radius: 50%;
    background: var(--accent);
  }
  .brand-name {
    position: absolute;
    left: 196px;
    top: 89px;
    margin: 0;
    font-family: "Open Sans", sans-serif;
    font-weight: 700;
    font-size: 46px;
    line-height: 56px;
    letter-spacing: 0;
  }
  .value-line {
    position: absolute;
    left: 97px;
    top: 176px;
    margin: 0;
    white-space: nowrap;
    font-family: "Open Sans", sans-serif;
    font-weight: 300;
    font-size: 48.5px;
    line-height: 58px;
    letter-spacing: -0.5px;
  }
  .value-line .figure {
    font-family: "Montserrat", sans-serif;
    font-weight: 800;
    font-style: italic;
    font-size: 45px;
    letter-spacing: 0;
  }
  .banner--dark .brand-name,
  .banner--dark .value-line { color: var(--ink-light); }
  .banner--dark .figure { color: var(--accent); }
  .banner--light .brand-name,
  .banner--light .value-line,
  .banner--light .figure { color: var(--ink-dark); }
</style>
</head>
<body>
<main class="canvas">
  <section class="banner banner--dark">
    <div class="tech-visual" role="img" aria-label="Abstract glowing circuit lines with translucent blue panels"></div>
    <div class="brand-mark"></div>
    <h1 class="brand-name">Varnel Brix</h1>
    <p class="value-line"><span class="figure">11,322</span> whitepapers from <span class="figure">726</span> companies.</p>
  </section>

  <section class="banner banner--light">
    <div class="tech-visual" role="img" aria-label="Abstract grey circuit lines with translucent grey panels"></div>
    <div class="brand-mark"></div>
    <h2 class="brand-name">Varnel Brix</h2>
    <p class="value-line"><span class="figure">11,322</span> whitepapers from <span class="figure">726</span> companies.</p>
  </section>
</main>
</body>
</html>
```